New Plumbing Company

We are looking for a smart and creative business card design for our new plumbing company. We are looking for creativity and originality in our business cards.

Industry/Entity Type

Plumbing

Contact Information for Business Card

Crestline Plumbing
Peter Halvane
Managing Director
Telephone Number : 0481529604
Email : service@crestlineplumbing.com.au
Website : www.crestlineplumbing.com.au
Lic. 508264K

Colors
0692cd
33a6d7
000000

Requirements
Must have
• I want the business card to be designed on a black background using the blue tones i have selected as seen in the company logo.

```html
<!DOCTYPE html>
<html lang="en">
<head>
<meta charset="UTF-8">
<title>Crestline Plumbing — Business Card</title>
<link href="https://fonts.googleapis.com/css2?family=Montserrat:wght@400;500;700&display=swap" rel="stylesheet">
<style>
  :root {
    --backdrop: #c9ddd2;
    --card-black: #000000;
    --blue-deep: #0692cd;
    --blue-light: #33a6d7;
    --white: #ffffff;
    --muted: #d8d8d8;
  }
  * { box-sizing: border-box; margin: 0; padding: 0; }
  html, body {
    width: 1200px;
    height: 1000px;
    overflow: hidden;
    background: var(--backdrop);
    font-family: "Montserrat", Arial, sans-serif;
  }
  .stage {
    width: 1200px;
    height: 1000px;
    display: flex;
    align-items: center;
    justify-content: center;
  }
  .business-card {
    position: relative;
    width: 840px;
    height: 480px;
    background: var(--card-black);
    border-radius: 44px;
    color: var(--white);
  }
  .brand-ring {
    position: absolute;
    left: 150px;
    top: 140px;
    width: 210px;
    height: 210px;
  }
  .info-block {
    position: absolute;
    left: 450px;
    top: 70px;
    width: 330px;
    text-align: center;
  }
  .company-name {
    font-weight: 500;
    font-size: 30px;
    letter-spacing: 1px;
    color: var(--blue-light);
    line-height: 1.1;
  }
  .person-name {
    margin-top: 26px;
    font-weight: 700;
    font-size: 30px;
    letter-spacing: 1.5px;
    color: var(--blue-deep);
  }
  .person-role {
    margin-top: 4px;
    font-size: 12px;
    letter-spacing: 4px;
    color: var(--muted);
  }
  .phone-line {
    margin-top: 14px;
    display: flex;
    align-items: center;
    justify-content: center;
    gap: 10px;
    font-weight: 500;
    font-size: 20px;
    letter-spacing: 1.5px;
    color: var(--blue-deep);
  }
  .phone-icon { width: 20px; height: 20px; }
  .contact-line {
    margin-top: 10px;
    font-size: 15px;
    letter-spacing: 1px;
    color: var(--muted);
  }
  .contact-line + .contact-line { margin-top: 4px; }
  .licence {
    margin-top: 6px;
    text-align: right;
    font-size: 11px;
    letter-spacing: 1px;
    color: var(--muted);
  }
</style>
</head>
<body>
  <main class="stage">
    <section class="business-card">
      <svg class="brand-ring" viewBox="0 0 210 210" aria-hidden="true">
        <circle cx="105" cy="105" r="96" fill="none" stroke="#33a6d7" stroke-width="10"/>
      </svg>
      <div class="info-block">
        <p class="company-name">Crestline Plumbing</p>
        <p class="person-name">Peter Halvane</p>
        <p class="person-role">MANAGING DIRECTOR</p>
        <p class="phone-line">
          <svg class="phone-icon" viewBox="0 0 20 20" aria-hidden="true">
            <circle cx="10" cy="10" r="10" fill="#0692cd"/>
            <path d="M6.2 5.5c.5-.4 1.2-.3 1.5.2l.9 1.6c.3.5.1 1-.3 1.3l-.6.4c.6 1.3 1.6 2.3 2.9 2.9l.4-.6c.3-.4.9-.6 1.3-.3l1.6.9c.5.3.6 1 .2 1.5l-.7.8c-.5.5-1.3.7-2 .4-2.8-1.1-5-3.3-6.1-6.1-.3-.7-.1-1.5.4-2z" fill="#000"/>
          </svg>
          <span>0481 529 604</span>
        </p>
        <p class="contact-line">service@crestlineplumbing.com.au</p>
        <p class="contact-line">www.crestlineplumbing.com.au</p>
        <p class="licence">Lic. 508264K</p>
      </div>
    </section>
  </main>
</body>
</html>
```